Stationary Package for New Bookkeeping Business

We need the following stationary designs:

- Business Card
- Letterhead
- With Comps
- Envelopes
- Paper Folder
- Email Signature

We will provide accounting and bookkeeping services to small business. We would like have the main color as blue and have a modern professional look.

Variations of colour and shades of blue welcome
Preference for deeper darker blue - navy

Variations of font in logo also welcome

Requirements
Must have
• Rosalind
B.Bus (Accounting)
Registered BAS Agent

Phone 0491 382 507
Post PO Box 947 Kelmora NSW 2768

Email rosalind@tarwinledgers.com

Business Card to be bold and eye catching

Should not have
• Letter head to not have too much colour on it

```html
<!DOCTYPE html>
<html lang="en">
<head>
<meta charset="utf-8">
<title>Tarwin Ledgers — Stationery Suite</title>
<link rel="stylesheet" href="https://fonts.googleapis.com/css2?family=Mulish:wght@400;600;700&display=swap">
<style>
  :root {
    --navy: #2c4a76;
    --navy-soft: #3f5c84;
    --navy-light: #52709a;
    --navy-deep: #263f66;
    --grey: #a9abae;
    --paper: #ffffff;
    --paper-shade: #f6f6f6;
    --backdrop: #ececec;
    --ink: #6a6d72;
  }
  * { margin: 0; padding: 0; box-sizing: border-box; }
  html, body { width: 1200px; height: 800px; overflow: hidden; }
  body {
    position: relative;
    background: var(--backdrop);
    font-family: "Mulish", Arial, sans-serif;
  }
  .piece { position: absolute; }

  /* name mark */
  .mark { display: flex; align-items: center; gap: 5px; color: var(--navy); font-weight: 600; line-height: 1.02; }
  .mark__square { background: var(--grey); flex: none; }
  .mark__name span { display: block; white-space: nowrap; }
  .mark--light { color: var(--paper); }
  .mark--light .mark__square { background: var(--paper); }

  /* letterhead */
  .letterhead { left: 95px; top: 98px; width: 307px; height: 432px; background: linear-gradient(180deg, var(--paper), var(--paper-shade)); }
  .letterhead .mark { position: absolute; left: 13px; top: 19px; font-size: 14.5px; }
  .letterhead .mark__square { width: 26px; height: 26px; }
  .bar { position: absolute; height: 5px; }
  .bar--grey { background: var(--grey); }
  .bar--navy { background: var(--navy); }
  .postal {
    position: absolute; left: 0; right: 0; text-align: center;
    color: var(--navy); font-weight: 700; font-size: 6.5px; letter-spacing: 0.9px; white-space: nowrap;
  }

  /* folders */
  .folder { background: var(--navy-soft); display: flex; align-items: center; justify-content: center; overflow: hidden; }
  .folder--front { left: 432px; top: 98px; width: 307px; height: 432px; }
  .folder--open { left: 780px; top: 73px; width: 335px; height: 462px; }
  .folder__pattern {
    position: absolute; inset: 0;
    background:
      radial-gradient(circle at 25% 15%, var(--navy-deep) 0 14%, transparent 30%),
      radial-gradient(circle at 75% 12%, var(--navy-deep) 0 12%, transparent 28%),
      radial-gradient(circle at 35% 88%, var(--navy-deep) 0 14%, transparent 30%),
      linear-gradient(135deg, var(--navy-light) 0%, var(--navy-soft) 30%, var(--navy-deep) 50%, var(--navy-soft) 70%, var(--navy-light) 100%);
  }
  .folder .mark { position: relative; font-size: 17px; }
  .folder .mark__square { width: 32px; height: 32px; }
  .folder__fold { position: absolute; left: 275px; top: 0; bottom: 0; width: 2px; background: var(--paper); }

  /* compliments slip */
  .comp-slip { left: 87px; top: 563px; width: 315px; height: 159px; background: linear-gradient(180deg, var(--paper), var(--paper-shade)); }
  .comp-slip .mark { position: absolute; left: 10px; top: 14px; font-size: 10.5px; }
  .comp-slip .mark__square { width: 19px; height: 19px; }

  /* envelope */
  .envelope { left: 436px; top: 560px; width: 317px; height: 162px; background: linear-gradient(180deg, var(--paper-shade), var(--paper)); }
  .envelope__flap { position: absolute; left: 0; top: 0; width: 317px; height: 36px; }
  .envelope__band { position: absolute; left: 0; right: 0; bottom: 2px; height: 9px; background: var(--navy); }
  .envelope__band .postal { color: var(--paper); top: 1px; font-size: 6px; }
  .envelope__square { position: absolute; left: 2px; bottom: 2px; width: 20px; height: 22px; background: var(--grey); }

  /* business cards */
  .card { width: 131px; height: 76px; }
  .card--front { left: 792px; top: 560px; background: var(--navy-soft); display: flex; align-items: center; justify-content: center; overflow: hidden; }
  .card--front .mark { position: relative; font-size: 8.5px; gap: 3px; }
  .card--front .mark__square { width: 15px; height: 15px; }
  .card--back { left: 980px; top: 558px; background: var(--paper); }
  .card--back .mark { position: absolute; left: 8px; top: 9px; font-size: 5.5px; gap: 3px; }
  .card--back .mark__square { width: 12px; height: 12px; }
  .card__name-band {
    position: absolute; left: 34px; right: 0; top: 21px; height: 12px; background: var(--navy);
    color: var(--paper); font-weight: 700; font-size: 8px; letter-spacing: 0.8px;
    text-align: right; padding-right: 6px; line-height: 12px;
  }
  .card__credentials { position: absolute; right: 6px; top: 37px; text-align: right; color: var(--ink); font-size: 4.4px; line-height: 1.35; letter-spacing: 0.3px; }
  .card__contact { position: absolute; left: 8px; top: 57px; color: var(--ink); font-size: 3.6px; line-height: 1.4; white-space: nowrap; }
  .card__contact b { color: var(--navy); }

  /* promotional items */
  .button { width: 34px; height: 34px; border-radius: 50%; background: var(--navy); top: 654px; }
  .pencil { left: 857px; top: 711px; width: 250px; height: 10px; }
</style>
</head>
<body>

  <section class="piece letterhead" aria-label="Letterhead">
    <div class="bar bar--grey" style="left:0;top:0;width:283px"></div>
    <div class="bar bar--navy" style="left:291px;top:0;width:14px"></div>
    <div class="mark"><div class="mark__square"></div><div class="mark__name"><span>Tarwin</span><span>Ledgers</span></div></div>
    <p class="postal" style="bottom:6px">POST PO BOX 947 KELMORA NSW 2768</p>
    <div class="bar bar--grey" style="left:0;bottom:0;width:15px;height:7px"></div>
    <div class="bar bar--navy" style="left:23px;bottom:0;width:284px;height:4px"></div>
  </section>

  <section class="piece folder folder--front" aria-label="Presentation folder cover">
    <div class="folder__pattern" role="img" aria-label="Large tonal navy pattern of finance symbols"></div>
    <div class="mark mark--light"><div class="mark__square"></div><div class="mark__name"><span>Tarwin</span><span>Ledgers</span></div></div>
  </section>

  <section class="piece folder folder--open" aria-label="Presentation folder with pocket">
    <div class="folder__pattern" role="img" aria-label="Large tonal navy pattern of finance symbols"></div>
    <div class="mark mark--light" style="left:-30px"><div class="mark__square"></div><div class="mark__name"><span>Tarwin</span><span>Ledgers</span></div></div>
    <div class="folder__fold"></div>
  </section>

  <section class="piece comp-slip" aria-label="With compliments slip">
    <div class="bar bar--grey" style="left:0;top:0;width:290px;height:4px"></div>
    <div class="bar bar--navy" style="left:298px;top:0;width:17px;height:4px"></div>
    <div class="mark"><div class="mark__square"></div><div class="mark__name"><span>Tarwin</span><span>Ledgers</span></div></div>
    <div class="bar bar--grey" style="left:0;bottom:0;width:20px;height:5px"></div>
    <div class="bar bar--navy" style="left:27px;bottom:0;width:288px;height:4px"></div>
  </section>

  <section class="piece envelope" aria-label="Envelope">
    <svg class="envelope__flap" viewBox="0 0 317 36" aria-hidden="true">
      <path d="M0 0H317V22Q317 34 300 34H17Q0 34 0 22Z" fill="var(--navy)"/>
    </svg>
    <div class="envelope__square"></div>
    <div class="envelope__band"><p class="postal">POST PO BOX 947 KELMORA NSW 2768</p></div>
  </section>

  <section class="piece card card--front" aria-label="Business card front">
    <div class="folder__pattern" role="img" aria-label="Tonal navy pattern of finance symbols"></div>
    <div class="mark mark--light"><div class="mark__square"></div><div class="mark__name"><span>Tarwin</span><span>Ledgers</span></div></div>
  </section>

  <section class="piece card card--back" aria-label="Business card back">
    <div class="mark"><div class="mark__square"></div><div class="mark__name"><span>Tarwin</span><span>Ledgers</span></div></div>
    <div class="card__name-band">ROSALIND</div>
    <p class="card__credentials">B.BUS (ACCOUNTING)<br>Registered BAS Agent</p>
    <p class="card__contact"><b>PHONE</b> 0491 382 507<br><b>POST</b> PO BOX 947 KELMORA NSW 2768<br><b>Email</b> rosalind@tarwinledgers.com</p>
  </section>

  <div class="piece button" style="left:941px"></div>
  <div class="piece button" style="left:1004px"></div>
  <div class="piece button" style="left:1068px"></div>

  <svg class="piece pencil" viewBox="0 0 250 10" aria-label="Branded pencil">
    <polygon points="0,5 14,1 14,9" fill="#d8c3a0"/>
    <polygon points="0,5 4,3.9 4,6.1" fill="#444"/>
    <rect x="14" y="1" width="236" height="8" rx="1.5" fill="var(--navy)"/>
  </svg>

</body>
</html>
```